A4 Childcare Spring Special Flyer

Crestwell Learning is a registered training organisation (RTO) Toid No. 47318, based in Blackburn, Victoria. We are a market leader in Professional development courses both accredited and non accredited, in order for you to maintain currency in your profession.

We need a flyer for a childcare specific spring special. The special is to offer a $50 VOLM gift card and 50% of your second training session. Conditions apply*

The training sessions available are the NEW childcare specific course: HLTAID004 Provide an emergency first aid response in an education and care setting and HLTAID003 Provide First Aid, HLTAID001 Provide Cardiopulmonary Resuscitation (CPR), 22024VIC Course in emergency management of asthma in the workplace
and 22099VIC Course in First Aid Management of Anaphylaxis.
We provide a flexible, cost effective and reliable service.
We have training locations available in Blackburn, Preston, Narre Warren and Mornington and can also provide onsite training.

We can also provide education and PRIVOS regulation consultation to the childcare provider.

Must use company logo, include phone number: (03) 5127 6481, website: www.crestwelllearning.com.au, email: marapenn@crestwelllearning.com.au

(Note that a letter with more detail will be attached with this flyer, therefore, with that in mind; use that information as desired).

The final product should be as childcare like as possible whilst also keeping our company colors (same as logo). We would also like for this flyer to stand out and be appealing to the recipient as this flyer is to gain potential clients, with emphasis on the HLTAID004 Course
Updates

Just need to update the qualifications: In the design brief I mentioned that the course; HLTAID001 Provide CPR and Asthma & Anaphyalxis.. Can this please be changed to HLTAID001 Provide Cardiopulmonary Resuscitation (CPR) And 22024VIC Course in emergency management of asthma in the workplace And 22099VIC Course in First Aid Management of Anaphylaxis (They are all singular courses) Apoligies!

Target Market(s)

Childcare centres, Out of school hours providers, pre-schools

Industry/Entity Type

Childcare

Font styles to use
Decorative

Colors
ffcf3e
f37123
faa54b

Requirements
Must have
• Company Logo
phone number
website
email
Registered Training Organisation
TOID: 47318

```html
<!DOCTYPE html>
<html lang="en">
<head>
<meta charset="utf-8">
<title>Crestwell Learning – Childcare Spring Special</title>
<link rel="stylesheet" href="https://fonts.googleapis.com/css2?family=Roboto:wght@700;900&family=PT+Sans:wght@400;700&family=PT+Sans+Narrow:wght@700&display=swap">
<style>
  :root {
    --orange: #f37123;
    --orange-deep: #f05a28;
    --amber: #faa54b;
    --yellow: #ffcf3e;
    --brown: #3a2a12;
    --ink: #333333;
    --grey: #555555;
    --red: #e8401c;
    --paper: #ffffff;
  }
  * { box-sizing: border-box; margin: 0; padding: 0; }
  html, body { width: 925px; height: 1200px; overflow: hidden; background: var(--paper); }
  .flyer { position: relative; width: 925px; height: 1200px; background: var(--paper); font-family: "PT Sans", sans-serif; color: var(--ink); }

  .masthead { position: absolute; left: 0; top: 0; width: 925px; height: 183px; background: var(--orange-deep);
    display: flex; align-items: center; justify-content: center; text-align: center; }
  .masthead h1 { font-family: "Roboto", sans-serif; font-weight: 700; font-size: 50px; line-height: 1.15; color: #fff;
    text-shadow: 2px 3px 4px rgba(0,0,0,.45); }

  .course-band { position: absolute; left: 0; top: 183px; width: 925px; height: 55px; background: var(--yellow);
    display: flex; align-items: center; justify-content: space-between; padding: 0 44px 0 44px;
    font-family: "Roboto", sans-serif; font-weight: 700; font-size: 32px; color: var(--brown); }

  .intro { position: absolute; left: 44px; top: 262px; width: 840px; font-size: 13.5px; line-height: 1.45; color: #555; }

  .benefits { position: absolute; left: 44px; top: 352px; width: 490px; list-style: none; }
  .benefits li { position: relative; padding-left: 34px; margin-bottom: 18px; font-size: 16.5px; font-weight: 700; line-height: 1.4; color: #444; }
  .benefits svg { position: absolute; left: 0; top: 2px; width: 22px; height: 22px; }

  .brand { position: absolute; left: 560px; top: 380px; width: 320px; text-align: center; }
  .brand-dot { width: 150px; height: 150px; border-radius: 50%; background: var(--orange); margin: 0 auto 40px; }
  .brand-name { font-family: "PT Sans", sans-serif; font-weight: 400; font-size: 46px; line-height: 1.05; color: var(--orange); }

  .offer { position: absolute; left: 52px; top: 563px; width: 385px; height: 232px; background: var(--yellow); border-radius: 14px;
    box-shadow: 0 6px 10px rgba(0,0,0,.3); text-align: center; padding-top: 14px; color: var(--brown); }
  .offer h2 { font-family: "PT Sans Narrow", sans-serif; font-weight: 700; font-size: 42px; line-height: 1.18; }
  .offer p { font-family: "PT Sans Narrow", sans-serif; font-weight: 700; font-size: 24px; line-height: 1.3; margin-top: 10px; }
  .offer .conditions { font-family: "PT Sans", sans-serif; font-weight: 400; font-size: 14px; color: var(--red); margin-top: 4px; }

  .toid { position: absolute; left: 52px; top: 812px; width: 385px; text-align: center; font-family: "PT Sans", sans-serif; font-weight: 700; font-size: 30px; color: var(--grey); }

  .contact { position: absolute; left: 500px; top: 755px; width: 400px; text-align: center; }
  .contact .phone { font-size: 24px; color: #222; }
  .contact .phone strong { font-size: 27px; }
  .contact .web { font-weight: 700; font-size: 28px; color: var(--red); margin-top: 12px; }
  .contact .email { font-size: 19px; font-weight: 700; color: #333; margin-top: 8px; }

  .photo { position: absolute; top: 872px; height: 328px; }
  .photo-carer { left: 0; width: 279px; background: linear-gradient(160deg, #8a5a3a 0%, #d9b99a 50%, #e6c2b0 100%); }
  .photo-kids { left: 279px; width: 646px; background: linear-gradient(180deg, #e85a3a 0%, #f08a6a 55%, #e9a6b0 100%); }
</style>
</head>
<body>
<main class="flyer">
  <header class="masthead">
    <h1>Crestwell Learning is a Registered<br>Training Organisation (RTO)</h1>
  </header>

  <div class="course-band">
    <span>HLTAID004 COURSE</span>
    <span>Blackburn, Victoria</span>
  </div>

  <p class="intro">The training sessions available are the NEW childcare specific course: HLTAID004 Provide an emergency first aid response in an education and care setting and HLTAID003 Provide First Aid, HLTAID001 Provide Cardiopulmonary Resuscitation (CPR) And 22024VIC Course in emergency management of asthma in the workplace And 22099VIC Course in First Aid Management of Anaphylaxis</p>

  <ul class="benefits">
    <li><svg viewBox="0 0 22 22"><rect x="1" y="3" width="17" height="17" rx="3" fill="none" stroke="#f05a28" stroke-width="2"/><path d="M5 11l4 4 11-12" fill="none" stroke="#f05a28" stroke-width="3" stroke-linecap="round" stroke-linejoin="round"/></svg>We provide a flexible, cost effective and reliable service.</li>
    <li><svg viewBox="0 0 22 22"><rect x="1" y="3" width="17" height="17" rx="3" fill="none" stroke="#f05a28" stroke-width="2"/><path d="M5 11l4 4 11-12" fill="none" stroke="#f05a28" stroke-width="3" stroke-linecap="round" stroke-linejoin="round"/></svg>We have training locations available in Blackburn, Preston, Narre Warren and Mornington and can also provide onsite training.</li>
    <li><svg viewBox="0 0 22 22"><rect x="1" y="3" width="17" height="17" rx="3" fill="none" stroke="#f05a28" stroke-width="2"/><path d="M5 11l4 4 11-12" fill="none" stroke="#f05a28" stroke-width="3" stroke-linecap="round" stroke-linejoin="round"/></svg>We can also provide education and PRIVOS regulation consultation to the childcare provider.</li>
  </ul>

  <div class="brand">
    <div class="brand-dot"></div>
    <div class="brand-name">Crestwell Learning</div>
  </div>

  <section class="offer">
    <h2>Childcare Specific<br>Spring Special OFFER</h2>
    <p>Offer a $50 VOLM gift card and 50%<br>of your second training session</p>
    <div class="conditions">Conditions apply*</div>
  </section>

  <div class="toid">Toid No. 47318</div>

  <address class="contact" style="font-style:normal">
    <div class="phone">Contact us: <strong>(03) 5127 6481</strong></div>
    <div class="web">www.crestwelllearning.com.au</div>
    <div class="email">email: marapenn@crestwelllearning.com.au</div>
  </address>

  <div class="photo photo-carer" role="img" aria-label="Photo of a carer sitting with a young girl indoors"></div>
  <div class="photo photo-kids" role="img" aria-label="Photo of happy children cheering with arms raised in a colourful play room"></div>
</main>
</body>
</html>
```